KRV Ltd Business Card
Professional Biz Card for Kestrel Ridge Ventures IBC Ltd
KRV Ltd Business Card -
Creative Brief
Professional
Milo Harwick
President & CEO
milo@kestrelridgeventures.biz
www.kestrelridgeventures.biz
Skype ID: mharwick should be added.
www.kestrelridgeventures.biz & perhaps a large version of my logo.

```html
<!DOCTYPE html>
<html lang="en">
<head>
<meta charset="utf-8">
<title>KRV Ltd Business Card</title>
<link rel="stylesheet" href="https://fonts.googleapis.com/css2?family=Open+Sans:wght@400;600;700;800&display=swap">
<style>
  :root {
    --page: #ffffff;
    --ink: #1a1a1a;
    --ink-soft: #444444;
    --card-dark-top: #2b2b2b;
    --card-dark-bottom: #0b0b0b;
    --card-light-top: #f7f7f7;
    --card-light-bottom: #d6d6d6;
    --mark-on-light: #8c8c8c;
    --mark-on-dark: #c9c9c9;
    --mark-split: #9a9a9a;
    --url-on-dark: #e6e6e6;
  }
  * { margin: 0; padding: 0; box-sizing: border-box; }
  html, body { width: 1200px; height: 734px; overflow: hidden; background: var(--page); }
  body { position: relative; font-family: "Open Sans", Arial, sans-serif; color: var(--ink); }

  .card {
    position: absolute;
    border-radius: 26px;
    overflow: hidden;
    box-shadow: 0 3px 10px rgba(0,0,0,0.28);
  }
  .card--front { left: 468px; top: 12px; width: 468px; height: 288px;
    background: linear-gradient(160deg, var(--card-light-top), var(--card-light-bottom)); }
  .card--back-light { left: 19px; top: 336px; width: 557px; height: 343px;
    background: linear-gradient(160deg, var(--card-light-top), var(--card-light-bottom)); }
  .card--back-dark { left: 619px; top: 336px; width: 562px; height: 343px;
    background: linear-gradient(160deg, var(--card-dark-top), var(--card-dark-bottom)); }

  .front-panel { position: absolute; inset: 0; }

  .identity { position: absolute; right: 26px; top: 22px; text-align: right; }
  .identity__name { font-size: 19px; font-weight: 700; line-height: 1.2; }
  .identity__title { font-size: 10px; color: var(--ink-soft); margin-top: 2px; }

  .contact { position: absolute; right: 26px; top: 176px; text-align: right;
    font-size: 10.5px; line-height: 1.55; color: var(--ink); }
  .contact b { font-weight: 700; }

  .wordmark { position: absolute; font-weight: 800; letter-spacing: 10px; line-height: 1; }
  .wordmark--front { left: 48px; top: 186px; font-size: 70px; color: var(--mark-split); }
  .wordmark--back { left: 0; right: 0; top: 126px; text-align: center; font-size: 96px; padding-left: 10px; }
  .card--back-light .wordmark--back { color: var(--mark-on-light); }
  .card--back-dark .wordmark--back { color: var(--mark-on-dark); }

  .site { position: absolute; left: 0; right: 0; bottom: 16px; text-align: center;
    font-size: 10px; font-weight: 600; }
  .card--back-light .site { color: var(--ink); }
  .card--back-dark .site { color: var(--url-on-dark); }
</style>
</head>
<body>

  <section class="card card--front">
    <svg class="front-panel" width="468" height="288" viewBox="0 0 468 288">
      <defs>
        <linearGradient id="darkPanel" x1="0" y1="0" x2="1" y2="1">
          <stop offset="0" stop-color="#2b2b2b"/>
          <stop offset="1" stop-color="#0b0b0b"/>
        </linearGradient>
        <linearGradient id="edgeSheen" x1="0" y1="0" x2="0" y2="1">
          <stop offset="0" stop-color="#ffffff" stop-opacity="0.2"/>
          <stop offset="0.55" stop-color="#ffffff" stop-opacity="0.9"/>
          <stop offset="1" stop-color="#bbbbbb" stop-opacity="0.6"/>
        </linearGradient>
      </defs>
      <path d="M0 0 H138 C150 70 120 130 150 190 C170 235 190 260 196 288 H0 Z" fill="url(#darkPanel)"/>
      <path d="M138 0 C150 70 120 130 150 190 C170 235 190 260 196 288" fill="none" stroke="url(#edgeSheen)" stroke-width="5"/>
    </svg>

    <div class="identity">
      <div class="identity__name">Milo Harwick</div>
      <div class="identity__title">President &amp; CEO</div>
    </div>

    <div class="contact">
      <div><b>C</b> : +86 139 2047 5162</div>
      <div><b>E</b> : milo@kestrelridgeventures.biz</div>
      <div><b>W</b> : www.kestrelridgeventures.biz</div>
      <div><b>Skype</b> : mharwick</div>
    </div>

    <div class="wordmark wordmark--front">KRV</div>
  </section>

  <section class="card card--back-light">
    <div class="wordmark wordmark--back">KRV</div>
    <div class="site">www.kestrelridgeventures.biz</div>
  </section>

  <section class="card card--back-dark">
    <div class="wordmark wordmark--back">KRV</div>
    <div class="site">www.kestrelridgeventures.biz</div>
  </section>

</body>
</html>
```